Business Cards for Mortgage Company
Modern Design
Professional
Dorel Maskovin
President
48877 Birch Hollow Road, Suite 410
Lake Forest, CA 92630
(800) 555-0147 ext. 2204
dmaskovin@qarvelfund.com
www.qarvelfund.com
NMLS# 604392
Please use the same font and colors as the attached Logo.

```html
<!DOCTYPE html>
<html lang="en">
<head>
<meta charset="utf-8">
<title>QarvelFund Business Cards</title>
<link href="https://fonts.googleapis.com/css2?family=Lato:wght@400;700&display=swap" rel="stylesheet">
<style>
  :root {
    --bg: #e9e9e7;
    --card: #ffffff;
    --green: #4ba52e;
    --green-dark: #2f8a1c;
    --green-light: #62c13f;
    --blue: #1f9bd7;
    --text: #555555;
    --muted: #8a8a8a;
    --rule: #cfcfcf;
  }
  * { margin: 0; padding: 0; box-sizing: border-box; }
  html, body { width: 1200px; height: 720px; overflow: hidden; }
  body { background: var(--bg); font-family: "Lato", sans-serif; position: relative; }

  .card { position: absolute; background: var(--card); box-shadow: 0 2px 8px rgba(0,0,0,0.18); overflow: hidden; }

  /* front card */
  .card-front { left: 40px; top: 350px; width: 560px; height: 310px; }
  .brand { font-weight: 700; color: var(--green); letter-spacing: -0.5px; display: flex; align-items: center; gap: 10px; }
  .brand-mark { width: 12px; height: 12px; background: currentColor; border-radius: 50%; }
  .card-front .brand { position: absolute; left: 50px; top: 48px; font-size: 46px; }
  .details { position: absolute; left: 50px; top: 140px; display: flex; }
  .person { width: 190px; padding-right: 14px; border-right: 1px solid var(--rule); }
  .person-name { color: var(--green); font-weight: 700; font-size: 15px; }
  .person-title { color: var(--blue); font-size: 13px; margin-bottom: 12px; }
  .address { color: var(--text); font-size: 12.5px; line-height: 1.45; }
  .contacts { list-style: none; padding-left: 14px; color: var(--text); font-size: 12.5px; line-height: 1.55; }
  .contacts li { display: flex; align-items: center; gap: 7px; }
  .contacts svg { width: 11px; height: 11px; fill: var(--green); flex: none; }
  .band { position: absolute; left: 0; bottom: 22px; width: 100%; height: 26px; background: var(--blue); }
  .band-accent { position: absolute; left: 0; bottom: 22px; width: 100%; height: 26px; }
  .band-url { position: absolute; left: 0; right: 0; bottom: 22px; height: 26px; line-height: 26px; text-align: center; color: #fff; font-size: 13px; letter-spacing: 2px; }

  /* white back */
  .card-back-white { left: 640px; top: 40px; width: 520px; height: 300px; }
  .card-back-white .brand { position: absolute; left: 0; right: 0; top: 92px; justify-content: center; font-size: 56px; }
  .card-back-white .url { position: absolute; left: 0; right: 0; top: 186px; text-align: center; color: var(--text); font-size: 14px; letter-spacing: 3px; }

  /* green back */
  .card-back-green { left: 640px; top: 380px; width: 520px; height: 300px; background: radial-gradient(ellipse at 50% 40%, var(--green-light), var(--green-dark) 85%); }
  .card-back-green .brand { position: absolute; left: 0; right: 0; top: 100px; justify-content: center; font-size: 52px; color: #fff; }
  .card-back-green .url { position: absolute; left: 0; right: 0; bottom: 40px; text-align: center; color: #fff; font-size: 13px; letter-spacing: 3px; }
</style>
</head>
<body>

<section class="card card-front">
  <div class="brand"><span class="brand-mark"></span>QarvelFund</div>
  <div class="details">
    <div class="person">
      <p class="person-name">Dorel Maskovin</p>
      <p class="person-title">President</p>
      <p class="address">48877 Birch Hollow Road<br>Suite 410, Lake Forest<br>CA 92630</p>
    </div>
    <ul class="contacts">
      <li><svg viewBox="0 0 12 12"><path d="M2 1h3l1 3-1.5 1a6 6 0 0 0 2.5 2.5L8 6l3 1v3a1 1 0 0 1-1 1A9 9 0 0 1 1 2a1 1 0 0 1 1-1z"/></svg>(800) 555-0147 ext. 2204</li>
      <li><svg viewBox="0 0 12 12"><rect x="3" y="0.5" width="6" height="11" rx="1"/></svg>(949) 555-0183</li>
      <li><svg viewBox="0 0 12 12"><rect x="1" y="4" width="10" height="7" rx="1"/><rect x="3" y="1" width="6" height="3"/></svg>(800) 555-0162</li>
      <li><svg viewBox="0 0 12 12"><path d="M1 2h10v8H1z M1 2l5 4 5-4" stroke="#fff" stroke-width="0.8"/></svg>dmaskovin@qarvelfund.com</li>
      <li>Lic No.: NMLS# 604392</li>
    </ul>
  </div>
  <div class="band"></div>
  <svg class="band-accent" viewBox="0 0 560 26" preserveAspectRatio="none"><polygon points="0,0 100,0 78,26 0,26" fill="var(--green)"/></svg>
  <p class="band-url">www.qarvelfund.com</p>
</section>

<section class="card card-back-white">
  <div class="brand"><span class="brand-mark"></span>QarvelFund</div>
  <p class="url">www.qarvelfund.com</p>
</section>

<section class="card card-back-green">
  <div class="brand"><span class="brand-mark"></span>QarvelFund</div>
  <p class="url">www.qarvelfund.com</p>
</section>

</body>
</html>
```